Fire and Building compliance company needs website

A professional website is needed for Kestow Alarm and Guard 2012 , company profile attached- we have a website but it is old and needs replacing (in fact we can not access it at present).

We are also looking at getting logo redesigned and will probably change to a flame type graphic with the letters KAG and then Fire and Building Compliance (bellow KAG).

It Company

• Ease of use
Page should fit inside typical screen size (not have to scroll down to see page).
Be made in Pagewright 2.5

search words- Wanganui, fire alarm, building compliance, building warrant of fitness,BWOF, burglar alarm systems, LPG refilling,fire extinguishers, emergency lighting.

```html
<!DOCTYPE html>
<html lang="en">
<head>
<meta charset="utf-8">
<title>Kestow Alarm and Guard 2012</title>
<link rel="stylesheet" href="https://fonts.googleapis.com/css2?family=Questrial&display=swap">
<style>
  :root {
    --ink: #141516;
    --paper: #ffffff;
    --band-dark: #3f4244;
    --band-mid: #7b7f80;
    --band-green: #4f7a2c;
    --pill-deep: #1b82c4;
    --pill-light: #6cc3ee;
    --field: #a9abae;
    --flame: #e4572a;
    --photo-top: #3d5a2c;
    --photo-bottom: #6f7276;
  }
  * { box-sizing: border-box; margin: 0; padding: 0; }
  html, body { width: 1200px; height: 998px; overflow: hidden; }
  body {
    position: relative;
    background: var(--ink);
    color: var(--paper);
    font-family: "Questrial", "Century Gothic", sans-serif;
  }
  .header { position: absolute; left: 0; top: 0; width: 1200px; height: 356px; background: var(--ink); }
  .welcome { position: absolute; left: 38px; top: 48px; font-size: 108px; font-weight: 400; letter-spacing: -1px; line-height: 1; }
  .tagline { position: absolute; left: 40px; top: 180px; font-size: 29px; line-height: 1.1; }
  .background-copy { position: absolute; left: 40px; top: 238px; width: 802px; font-size: 16.5px; line-height: 22.6px; text-align: justify; text-align-last: justify; }
  .background-copy .label { display: block; letter-spacing: 0; }
  .brand { position: absolute; left: 922px; top: 50px; width: 236px; height: 292px; display: flex; align-items: center; justify-content: center; gap: 14px; }
  .brand-dot { width: 26px; height: 26px; border-radius: 50%; background: var(--flame); }
  .brand-name { font-size: 64px; color: var(--flame); line-height: 1; }

  .stage {
    position: absolute; left: 0; top: 356px; width: 1200px; height: 556px;
    background:
      linear-gradient(180deg, transparent 0 6%, rgba(79,122,44,.55) 9%, transparent 13%, transparent 33%, rgba(79,122,44,.45) 37%, transparent 41%, transparent 50%, rgba(90,110,40,.6) 55%, transparent 60%),
      linear-gradient(180deg, var(--band-dark) 0%, var(--band-mid) 30%, var(--band-dark) 55%, var(--band-mid) 80%, var(--band-dark) 100%);
  }
  .photo {
    position: absolute; left: 376px; top: 22px; width: 736px; height: 512px;
    background: linear-gradient(180deg, var(--photo-top) 0%, #4d6244 40%, var(--photo-bottom) 62%, #5e6165 100%);
  }
  .nav { position: absolute; left: 40px; top: 28px; list-style: none; }
  .nav-item { position: absolute; left: 0; width: 202px; height: 44px; }
  .nav-item:nth-child(1) { top: 0; }
  .nav-item:nth-child(2) { top: 62px; }
  .nav-item:nth-child(3) { top: 122px; }
  .nav-item:nth-child(4) { top: 210px; }
  .pill { position: absolute; inset: 0; }
  .nav-label { position: absolute; left: 62px; top: 6px; font-size: 28px; line-height: 1.1; }
  .nav-item.small .nav-label { left: 48px; top: 9px; font-size: 25px; }

  .note { position: absolute; left: 40px; top: 336px; font-size: 30px; line-height: 40px; width: 560px; }

  .member { position: absolute; left: 727px; top: 364px; width: 360px; }
  .member-title { font-size: 26px; line-height: 1; }
  .field-row { position: absolute; left: 0; width: 350px; height: 38px; }
  .field-row.email { top: 40px; }
  .field-row.search { top: 90px; }
  .field-label { position: absolute; left: 26px; top: 4px; font-size: 27px; line-height: 1.1; }
  .field-row.search .field-label { left: 26px; top: 5px; font-size: 25px; }
  .field-input { position: absolute; left: 120px; top: 11px; width: 145px; height: 16px; background: var(--field); border: 1px solid #e9eaeb; }

  .footer { position: absolute; left: 0; top: 912px; width: 1200px; height: 86px; background: var(--ink); }
  .copyright { position: absolute; left: 0; width: 1270px; top: 16px; text-align: center; font-size: 21px; }
</style>
</head>
<body>
  <svg width="0" height="0" style="position:absolute">
    <defs>
      <linearGradient id="pillFill" x1="0" x2="1" y1="0" y2="0">
        <stop offset="0" stop-color="#1576ba"/>
        <stop offset="1" stop-color="#79c9f0"/>
      </linearGradient>
      <symbol id="pillShape" viewBox="0 0 202 44" preserveAspectRatio="none">
        <path d="M22 1 H150 C185 1 202 14 202 22 C202 30 185 43 150 43 H22 A21 21 0 0 1 22 1 Z" fill="url(#pillFill)"/>
      </symbol>
      <symbol id="flameBadge" viewBox="0 0 44 44">
        <circle cx="22" cy="22" r="19" fill="#ffffff"/>
        <circle cx="22" cy="24" r="13" fill="#e4572a"/>
      </symbol>
    </defs>
  </svg>

  <header class="header">
    <h1 class="welcome">Welcome</h1>
    <p class="tagline">Kestow Alarm and Guard 2012.</p>
    <p class="background-copy">
      <span class="label">B A C K G R O U N D</span>
      Kestow Alarm &amp; Guard is a locally owned and operated fire protection company. Since 1978 we have evolved and developed to suit the demands of our clients and the 1992 Building Compiance Act. This ability to alter and change as required means that we are now viewed as an innovative and contemporary company.
    </p>
    <div class="brand">
      <span class="brand-dot"></span>
      <span class="brand-name">KAG</span>
    </div>
  </header>

  <main class="stage" role="img" aria-label="Blurred grey and green motion backdrop">
    <div class="photo" role="img" aria-label="Photo of a fire extinguisher training demonstration outdoors"></div>

    <ul class="nav">
      <li class="nav-item"><svg class="pill" viewBox="0 0 202 44"><use href="#pillShape"/><use href="#flameBadge" x="0" y="0" width="44" height="44"/></svg><span class="nav-label">Home</span></li>
      <li class="nav-item"><svg class="pill" viewBox="0 0 202 44"><use href="#pillShape"/><use href="#flameBadge" x="0" y="0" width="44" height="44"/></svg><span class="nav-label">Product</span></li>
      <li class="nav-item"><svg class="pill" viewBox="0 0 202 44"><use href="#pillShape"/><use href="#flameBadge" x="0" y="0" width="44" height="44"/></svg><span class="nav-label">News</span></li>
      <li class="nav-item small"><svg class="pill" viewBox="0 0 202 44"><use href="#pillShape"/><use href="#flameBadge" x="0" y="0" width="44" height="44"/></svg><span class="nav-label">Contact us</span></li>
    </ul>

    <p class="note">NB:<br>This is the main theme of<br>your new website. You can fill with all<br>your conten in Pagewright. Thank you..</p>

    <form class="member">
      <p class="member-title">Member login/Sign up</p>
      <div class="field-row email">
        <svg class="pill" viewBox="0 0 350 38" preserveAspectRatio="none"><path d="M18 1 H280 C330 1 350 12 350 19 C350 26 330 37 280 37 H18 A18 18 0 0 1 18 1 Z" fill="url(#pillFill)"/><circle cx="299" cy="19" r="13" fill="#ffffff"/><circle cx="299" cy="21" r="8.5" fill="#e4572a"/></svg>
        <span class="field-label">Email</span>
        <span class="field-input"></span>
      </div>
      <div class="field-row search">
        <svg class="pill" viewBox="0 0 350 38" preserveAspectRatio="none"><path d="M18 1 H280 C330 1 350 12 350 19 C350 26 330 37 280 37 H18 A18 18 0 0 1 18 1 Z" fill="url(#pillFill)"/><circle cx="299" cy="19" r="13" fill="#ffffff"/><circle cx="299" cy="21" r="8.5" fill="#e4572a"/></svg>
        <span class="field-label">Search</span>
        <span class="field-input"></span>
      </div>
    </form>
  </main>

  <footer class="footer">
    <p class="copyright">Copyright 2013.</p>
  </footer>
</body>
</html>
```